ultra-minimalist business card

front (black background, matte):

tarik b. hosseny
writer | photographer
get@tarikhosseny.com

back (white background, matte):

a picture speaks a thousand words;
a word draws a thousand pictures.

www.tarikhosseny.com

all text should be small (white or silver - as long as it shows against the black - on the front; black or gray - as long as it shows against the white - on the back).

feel free to get creative in terms of arrangement, alignment, and font type, but remember, the overall style is minimalist, so nothing too fancy, please.

thanks.

```html
<!DOCTYPE html>
<html lang="en">
<head>
<meta charset="utf-8">
<title>tarik b. hosseny — business card</title>
<link rel="stylesheet" href="https://fonts.googleapis.com/css2?family=EB+Garamond:wght@400;700&family=Raleway:wght@300;400&display=swap">
<style>
  :root {
    --backdrop: #555555;
    --card-front: #000000;
    --card-back: #ffffff;
    --ink-light: #f2f2f2;
    --ink-silver: #c9c9c9;
    --ink-dark: #2b2b2b;
    --ink-gray: #9a9a9a;
    --dot-front: #d4d4d4;
    --dot-back: #c8c8c8;
    --rule-front: #5a5a5a;
    --rule-back: #cfcfcf;
  }
  * { margin: 0; padding: 0; box-sizing: border-box; }
  html, body {
    width: 1200px; height: 1200px; overflow: hidden;
    background: var(--backdrop);
  }
  .canvas { position: relative; width: 1200px; height: 1200px; }

  .card {
    position: absolute; left: 198px; width: 780px; height: 468px;
  }
  .card--front { top: 96px; background: var(--card-front); }
  .card--back { top: 634px; background: var(--card-back); }

  .centered {
    position: absolute; left: 0; width: 100%;
    text-align: center; white-space: nowrap;
    transform: translateY(-50%);
  }

  .name {
    top: 192px;
    font-family: "EB Garamond", serif; font-weight: 400;
    font-size: 62px; color: var(--ink-light); letter-spacing: 0.5px;
  }
  .role {
    top: 240px;
    font-family: "Raleway", sans-serif; font-weight: 300;
    font-size: 19px; color: var(--ink-silver); letter-spacing: 0.3px;
  }
  .role-rule {
    position: absolute; top: 241px; height: 1px; width: 152px;
  }
  .role-rule--left { left: 126px; background: linear-gradient(to right, transparent, var(--rule-front)); }
  .role-rule--right { left: 502px; background: linear-gradient(to left, transparent, var(--rule-front)); }

  .contact-row {
    position: absolute; top: 400px; left: 0; width: 100%;
    display: flex; justify-content: center; align-items: center;
    transform: translateY(-50%);
  }
  .contact-row__text {
    font-family: "Raleway", sans-serif; font-weight: 400;
    font-size: 14.5px; margin: 0 20px; white-space: nowrap;
  }
  .card--front .contact-row__text { color: var(--ink-silver); }
  .card--back .contact-row__text { color: var(--ink-gray); font-size: 16px; }

  .dots { display: flex; align-items: center; gap: 17px; }
  .dot { border-radius: 50%; display: block; }
  .card--front .dot { background: var(--dot-front); }
  .card--back .dot { background: var(--dot-back); }
  .dot--1 { width: 4px; height: 4px; }
  .dot--2 { width: 6px; height: 6px; }
  .dot--3 { width: 9px; height: 9px; }
  .dot--4 { width: 11px; height: 11px; }
  .dot--5 { width: 13px; height: 13px; }

  .quote-lead {
    font-family: "EB Garamond", serif; font-weight: 400;
    font-size: 33px; color: var(--ink-dark);
  }
  .quote-key {
    font-family: "EB Garamond", serif; font-weight: 700;
    font-size: 32px; color: var(--ink-dark); letter-spacing: 0.5px;
  }
  .quote-lead--first { top: 104px; }
  .quote-key--first { top: 142px; }
  .quote-lead--second { top: 266px; }
  .quote-key--second { top: 304px; }

  .divider { position: absolute; left: 126px; top: 200px; }
</style>
</head>
<body>
<main class="canvas">

  <section class="card card--front" aria-label="Card front">
    <h1 class="centered name">tarik b. hosseny</h1>
    <span class="role-rule role-rule--left"></span>
    <p class="centered role">writer | photographer</p>
    <span class="role-rule role-rule--right"></span>

    <div class="contact-row">
      <span class="dots"><i class="dot dot--1"></i><i class="dot dot--2"></i><i class="dot dot--3"></i><i class="dot dot--4"></i><i class="dot dot--5"></i></span>
      <span class="contact-row__text">contact me at: get@tarikhosseny.com</span>
      <span class="dots"><i class="dot dot--5"></i><i class="dot dot--4"></i><i class="dot dot--3"></i><i class="dot dot--2"></i><i class="dot dot--1"></i></span>
    </div>
  </section>

  <section class="card card--back" aria-label="Card back">
    <p class="centered quote-lead quote-lead--first">a picture speaks a</p>
    <p class="centered quote-key quote-key--first">THOUSAND WORDS</p>

    <svg class="divider" width="532" height="22" viewBox="0 0 532 22" aria-hidden="true">
      <defs>
        <linearGradient id="rule-fade-left" x1="0" x2="1">
          <stop offset="0" stop-color="#cfcfcf" stop-opacity="0"/>
          <stop offset="1" stop-color="#cfcfcf"/>
        </linearGradient>
        <linearGradient id="rule-fade-right" x1="1" x2="0">
          <stop offset="0" stop-color="#cfcfcf" stop-opacity="0"/>
          <stop offset="1" stop-color="#cfcfcf"/>
        </linearGradient>
      </defs>
      <rect x="0" y="10.5" width="255" height="1" fill="url(#rule-fade-left)"/>
      <rect x="277" y="10.5" width="255" height="1" fill="url(#rule-fade-right)"/>
      <rect x="258.5" y="3.5" width="15" height="15" transform="rotate(45 266 11)" fill="#ffffff" stroke="#c4c4c4" stroke-width="1.5"/>
    </svg>

    <p class="centered quote-lead quote-lead--second">a word draws a</p>
    <p class="centered quote-key quote-key--second">THOUSAND PICTURES</p>

    <div class="contact-row">
      <span class="dots"><i class="dot dot--1"></i><i class="dot dot--2"></i><i class="dot dot--3"></i><i class="dot dot--4"></i><i class="dot dot--5"></i></span>
      <span class="contact-row__text">www.tarikhosseny.com</span>
      <span class="dots"><i class="dot dot--5"></i><i class="dot dot--4"></i><i class="dot dot--3"></i><i class="dot dot--2"></i><i class="dot dot--1"></i></span>
    </div>
  </section>

</main>
</body>
</html>
```